Industrial / automotive service company
Renewing and reconditioning solutions
Simple
Ted Pelkin
VP - Industrial Division
217 Marston Crescent NW
Calgary, Alberta
T2P 4G6
t-pelkin@zorvamail.com

```html
<!DOCTYPE html>
<html lang="en">
<head>
<meta charset="UTF-8">
<title>Tovalmex Services Inc. – Business Card</title>
<link rel="stylesheet" href="https://fonts.googleapis.com/css2?family=Exo+2:wght@400;600;800&display=swap">
<style>
  :root {
    --brand-green: #8cc63f;
    --brand-green-dark: #77b02e;
    --ink-grey: #6d6e71;
    --ink-dark: #4a4b4d;
    --card-white: #ffffff;
    --backdrop: #eceeea;
  }
  * { box-sizing: border-box; margin: 0; padding: 0; }
  html, body {
    width: 1200px; height: 980px; overflow: hidden;
    background: var(--backdrop);
    font-family: "Exo 2", sans-serif;
  }
  .sheet {
    width: 1200px; height: 980px;
    display: flex; flex-direction: column;
    align-items: center; justify-content: center; gap: 22px;
  }
  .card {
    position: relative;
    width: 800px; height: 457px;
    border-radius: 22px;
    overflow: hidden;
    box-shadow: 0 6px 18px rgba(0,0,0,0.12);
  }
  .card--front { background: var(--card-white); }
  .card--back { background: var(--brand-green); }

  .card__curves { position: absolute; inset: 0; }

  .brand { position: absolute; left: 52px; top: 44px; }
  .brand__name {
    font-weight: 800; font-size: 58px; letter-spacing: 2px;
    color: var(--brand-green); line-height: 1;
    display: flex; align-items: center; gap: 14px;
  }
  .brand__dot {
    width: 20px; height: 20px; border-radius: 50%;
    background: var(--brand-green); flex: none;
  }
  .brand__sub {
    margin-top: 6px; margin-left: 120px;
    font-weight: 600; font-size: 22px; letter-spacing: 3px;
    color: var(--ink-grey);
  }

  .contact {
    position: absolute; left: 52px; top: 178px;
    list-style: none;
    font-size: 16px; letter-spacing: 1.5px; color: var(--ink-dark);
  }
  .contact__item { display: flex; align-items: center; gap: 10px; height: 27px; }
  .contact__item--plain { padding-left: 24px; }
  .contact__icon { width: 14px; height: 14px; flex: none; }

  .person {
    position: absolute; right: 250px; bottom: 66px; text-align: right;
  }
  .person__name {
    font-weight: 600; font-size: 22px; letter-spacing: 2px; color: var(--brand-green);
  }
  .person__title {
    margin-top: 4px; font-size: 15px; letter-spacing: 2px; color: var(--ink-grey);
  }

  .back-brand {
    position: absolute; left: 0; right: 0; top: 150px;
    display: flex; justify-content: center; align-items: center; gap: 16px;
    font-weight: 800; font-size: 64px; letter-spacing: 3px; color: var(--card-white);
  }
  .back-brand__dot {
    width: 22px; height: 22px; border-radius: 50%; background: var(--card-white);
  }
  .back-web {
    position: absolute; right: 58px; bottom: 52px;
    font-size: 18px; letter-spacing: 4px; color: var(--card-white);
  }
</style>
</head>
<body>
<main class="sheet">

  <section class="card card--front" aria-label="Business card front">
    <svg class="card__curves" viewBox="0 0 800 457" aria-hidden="true">
      <path d="M800 205 C700 260 640 360 622 457 L800 457 Z" fill="var(--brand-green)"/>
      <path d="M800 168 C690 225 610 340 588 457" fill="none" stroke="var(--brand-green)" stroke-width="7"/>
      <path d="M800 250 C730 300 690 380 680 457" fill="none" stroke="var(--card-white)" stroke-width="6"/>
    </svg>

    <div class="brand">
      <div class="brand__name"><span class="brand__dot"></span>TOVALMEX</div>
      <div class="brand__sub">SERVICES INC.</div>
    </div>

    <ul class="contact">
      <li class="contact__item">
        <svg class="contact__icon" viewBox="0 0 14 14"><path d="M7 1a4 4 0 0 1 4 4c0 3-4 8-4 8S3 8 3 5a4 4 0 0 1 4-4z" fill="var(--brand-green)"/><circle cx="7" cy="5" r="1.5" fill="#fff"/></svg>
        217 MARSTON CRESCENT NW
      </li>
      <li class="contact__item contact__item--plain">CALGARY, ALBERTA</li>
      <li class="contact__item contact__item--plain">T2P 4G6</li>
      <li class="contact__item">
        <svg class="contact__icon" viewBox="0 0 14 14"><circle cx="7" cy="7" r="7" fill="var(--brand-green)"/><path d="M4.5 3.5l1.6 0 .6 2-1 .8a5 5 0 0 0 2.4 2.4l.8-1 2 .6v1.6c-3.5.3-6.7-2.9-6.4-6.4z" fill="#fff"/></svg>
        (403) 555-0147
      </li>
      <li class="contact__item">
        <svg class="contact__icon" viewBox="0 0 14 14"><circle cx="7" cy="7" r="7" fill="var(--brand-green)"/><rect x="3.5" y="4.5" width="7" height="5" fill="#fff"/><path d="M3.5 4.5 7 7.5l3.5-3" fill="none" stroke="var(--brand-green)" stroke-width="0.9"/></svg>
        t-pelkin@zorvamail.com
      </li>
      <li class="contact__item">
        <svg class="contact__icon" viewBox="0 0 14 14"><circle cx="7" cy="7" r="7" fill="var(--brand-green)"/><circle cx="7" cy="7" r="3.6" fill="none" stroke="#fff" stroke-width="1"/><path d="M3.4 7h7.2M7 3.4v7.2" stroke="#fff" stroke-width="0.9"/></svg>
        www.tovalmexservices.com
      </li>
    </ul>

    <div class="person">
      <div class="person__name">TED PELKIN</div>
      <div class="person__title">VP - INDUSTRIAL DIVISION</div>
    </div>
  </section>

  <section class="card card--back" aria-label="Business card back">
    <div class="back-brand"><span class="back-brand__dot"></span>TOVALMEX</div>
    <div class="back-web">WWW.TOVALMEXSERVICES.COM</div>
  </section>

</main>
</body>
</html>
```